Not another boring Business Card Design Project

This is not another boring Business Card Design Project.

We are looking for the weirdest, wackiest most boundary pushing designs that you can come up with.

If you believe that design can be fun, energetic, crazy, unpredictable, beautiful and eye-catching then read on… this project is for you.

We are Tolvin Presk and we print plastic cards.

We are running a Plastic Card Design Competition.

And we need a plastic card to advertise the competition to graphic designers just like you.

The design needs to make your average designers’ jaws drop and their eyes pop out.

You can do what you wish with the card design, so long as it stands out.

We like these designs, designs that stretch the boundaries and become something beyond just another business card:

http://quorvamedia.net/wp-content/uploads/2009/03/b48.jpg
Designer - http://www.pelvanworks.com/

http://quorvamedia.net/wp-content/uploads/2009/03/b41.jpg
Designer - http://renolbrakstad.com/

http://images.plinthhive.com/designs/44195_732292_37774_thumbnail.jpg
Designer- Zentro Media at Plinth Hive

http://images.plinthhive.com/designs/44195_717529_37774_thumbnail.jpg
Designer - Zentro Media at Plinth Hive

http://quorvamedia.net/wp-content/uploads/2009/03/b11.jpg
Designer - http://www.wk7studio.com/

http://quorvamedia.net/wp-content/uploads/2009/03/b16.jpg
Designer - http://www.pebbletumbler.com/

Reason: A number of designers have said they want to submit designs and haven't yet done so, we want to give them time.

Reason: We've extended the deadline by 4 days for those who want to submit their designs over the weekend and give ourselves time to judge them

Plastic

• The design needs to contain this link: lnk.example/QzRpLk and any other detail that will encourage competition entry. The design will be printed on plastic.
• No borders (when plastic cards are punched to shape and size there is movement of 1 - 2mm, borders highlight this movement).

Keep text 3mm away from edges of the cards.

Please don't create designs to be produced on clear/transparent plastic.

```html
<!DOCTYPE html>
<html lang="en">
<head>
<meta charset="utf-8">
<title>Plastic Card Design Competition</title>
<link href="https://fonts.googleapis.com/css2?family=Aldrich&family=Share+Tech+Mono&display=swap" rel="stylesheet">
<style>
  :root {
    --page-bg: #e9e6e1;
    --card-dark: #1c1d1a;
    --card-olive: #4a4732;
    --glow-gold: rgba(181, 154, 60, 0.75);
    --glow-violet: rgba(107, 98, 144, 0.8);
    --ring-light: rgba(242, 241, 234, 0.45);
    --ring-soft: rgba(242, 241, 234, 0.12);
    --stripe: #f2f1ea;
    --tag-yellow: #e4e26a;
    --tag-pale: #d9d9dd;
    --ink: #0b0b0a;
  }
  * { margin: 0; padding: 0; box-sizing: border-box; }
  html, body { width: 1200px; height: 800px; overflow: hidden; background: var(--page-bg); }
  .canvas { position: relative; width: 1200px; height: 800px; }
  .card {
    position: absolute; left: 75px; top: 100px; width: 1050px; height: 600px;
    overflow: hidden; border-radius: 14px;
    background:
      radial-gradient(ellipse 420px 300px at 55% 28%, var(--glow-gold), transparent 70%),
      radial-gradient(ellipse 380px 260px at 88% 8%, var(--glow-violet), transparent 70%),
      linear-gradient(160deg, var(--card-olive) 0%, var(--card-dark) 70%);
  }
  .lettering-pattern {
    position: absolute; left: 0; top: 0; width: 1050px; height: 560px;
    background:
      linear-gradient(180deg, transparent 0%, rgba(30, 30, 26, 0.28) 20%, transparent 40%,
        rgba(30, 30, 26, 0.22) 55%, transparent 72%, rgba(30, 30, 26, 0.18) 85%, transparent 100%);
  }
  .ring-ornament {
    position: absolute; border-radius: 50%;
    background: radial-gradient(circle, var(--ring-soft) 0%, var(--ring-light) 55%, var(--ring-soft) 72%, transparent 74%);
  }
  .ring-ornament.left { left: 80px; top: 60px; width: 340px; height: 340px; }
  .ring-ornament.right { left: 475px; top: 35px; width: 330px; height: 330px; }
  .ring-ornament.bottom { left: -130px; top: 410px; width: 520px; height: 520px; opacity: 0.7; }
  .stripes { position: absolute; inset: 0; }
  .tag {
    position: absolute; background: var(--tag-yellow); color: var(--ink);
    font-family: "Share Tech Mono", monospace; font-size: 13px; line-height: 1; padding: 4px 8px;
    opacity: 0.9;
  }
  .tag.pale { background: var(--tag-pale); }
  .entry-link {
    position: absolute; left: 150px; top: 205px;
    font-family: "Aldrich", sans-serif; font-size: 76px; line-height: 1; color: var(--ink);
    letter-spacing: 3px; white-space: nowrap;
  }
</style>
</head>
<body>
<div class="canvas">
  <div class="card">
    <div class="lettering-pattern" role="img" aria-label="Faint repeated extruded lettering pattern"></div>

    <div class="ring-ornament left" role="img" aria-label="Concentric interface ring ornament"></div>
    <div class="ring-ornament right" role="img" aria-label="Concentric interface ring ornament"></div>
    <div class="ring-ornament bottom" role="img" aria-label="Large concentric interface ring ornament"></div>

    <svg class="stripes" width="1050" height="600" viewBox="0 0 1050 600" fill="none" stroke="var(--stripe)">
      <line x1="620" y1="420" x2="900" y2="420" stroke-width="5"/>
      <line x1="620" y1="436" x2="900" y2="436" stroke-width="5"/>
      <line x1="620" y1="452" x2="880" y2="452" stroke-width="5"/>
      <line x1="140" y1="330" x2="390" y2="330" stroke-width="3"/>
      <line x1="140" y1="342" x2="390" y2="342" stroke-width="3"/>
    </svg>

    <span class="tag" style="left:210px;top:165px;">01</span>
    <span class="tag" style="left:40px;top:330px;">001</span>
    <span class="tag pale" style="left:820px;top:20px;">001</span>
    <span class="tag pale" style="left:780px;top:110px;">001</span>
    <span class="tag" style="left:560px;top:320px;">001</span>
    <span class="tag" style="left:620px;top:350px;">001</span>
    <span class="tag" style="left:700px;top:380px;">001</span>

    <div class="entry-link">lnk.example/QzRpLk</div>
  </div>
</div>
</body>
</html>
```